Mental Health Therapy Website

I need a design for a mental health therapy website. It is a private practice. The business name is Brindle Counseling, PLLC. My name is Martin Hale, LMHC, NCC, DCC. I would like some of the features/menus to be Home; Welcome/About Me, Rates and Services, Common Questions, and Contact.
If possible I would like a blog on the main page that I can update with articles I write. I would like the contact page to feature a map to my location (4318 Cedarbend Ave. E, Lakewood, WA 98499).
I would like to place a small photo of me on the Welcome/About page.
I am new to this so if I am forgetting anything, please ask me!!
I will upload my logo so you can fit it and the color scheme into the design.
Thank you so very much!

```html
<!DOCTYPE html>
<html lang="en">
<head>
<meta charset="utf-8">
<title>Brindle Counseling, PLLC</title>
<link href="https://fonts.googleapis.com/css2?family=Open+Sans:wght@300;400;600;700&display=swap" rel="stylesheet">
<style>
  :root {
    --brand-blue: #2f6aa6;
    --brand-green: #5b9d3c;
    --ink: #333333;
    --muted: #8a8a8a;
    --line: #dddddd;
    --band: #f1f1f1;
    --page: #ffffff;
    --icon-dark: #3b3f44;
    --footer: #f7f7f7;
  }
  * { box-sizing: border-box; margin: 0; padding: 0; }
  html, body { width: 865px; height: 1200px; overflow: hidden; }
  body {
    background: var(--page);
    color: var(--ink);
    font-family: "Open Sans", Arial, sans-serif;
    font-size: 10px;
  }
  .site-header {
    height: 62px;
    display: flex; align-items: center; justify-content: space-between;
    padding: 0 44px;
    border-bottom: 1px solid var(--line);
  }
  .brand { display: flex; align-items: center; gap: 8px; }
  .brand-dot { width: 26px; height: 26px; border-radius: 50%; background: var(--brand-green); }
  .brand-name { font-size: 17px; font-weight: 600; color: var(--brand-blue); }
  .main-nav { display: flex; gap: 18px; }
  .main-nav a { color: var(--muted); text-decoration: none; font-size: 9.5px; font-weight: 600; letter-spacing: .4px; }
  .main-nav a.current { color: var(--brand-blue); }

  .hero {
    height: 270px; position: relative;
    background: linear-gradient(180deg, #eceeef 0%, #d9dcde 100%);
  }
  .hero-portrait {
    position: absolute; left: 180px; bottom: 0; width: 170px; height: 230px;
    background: linear-gradient(180deg, #5e8dc0 0%, #2f5f96 100%);
    border-radius: 85px 85px 0 0;
  }
  .hero-title {
    position: absolute; left: 300px; top: 150px;
    font-size: 30px; font-weight: 300; color: #ffffff; letter-spacing: 1px;
  }
  .hero-title b { font-weight: 700; }

  .section-title {
    text-align: center; font-size: 17px; font-weight: 700; letter-spacing: 1px;
    color: var(--ink); margin-bottom: 26px;
  }
  .section-title span { font-weight: 300; color: var(--muted); }

  .services { padding: 28px 60px 30px; height: 232px; }
  .service-grid { display: grid; grid-template-columns: repeat(4, 1fr); gap: 26px; }
  .service { text-align: center; }
  .service-icon {
    width: 46px; height: 46px; border-radius: 50%; background: var(--icon-dark);
    margin: 0 auto 14px; display: flex; align-items: center; justify-content: center;
  }
  .service h3 { font-size: 9.5px; font-weight: 700; margin-bottom: 7px; letter-spacing: .3px; }
  .service p { font-size: 8.5px; line-height: 1.55; color: var(--muted); }
  .read-more { display: inline-block; margin-top: 6px; font-size: 8.5px; color: var(--brand-blue); }

  .latest { background: var(--band); padding: 24px 60px; height: 172px; }
  .latest .section-title { margin-bottom: 20px; }
  .post-grid { display: grid; grid-template-columns: repeat(3, 1fr); gap: 30px; }
  .post { display: flex; gap: 12px; }
  .post-thumb {
    flex: 0 0 44px; height: 44px; border-radius: 50%;
    background: linear-gradient(135deg, #a9b4bd, #6f7c87);
  }
  .post h4 { font-size: 9px; font-weight: 700; margin-bottom: 5px; }
  .post p { font-size: 8.5px; line-height: 1.5; color: var(--muted); }

  .contact { padding: 26px 60px 0; height: 400px; }
  .contact .section-title { margin-bottom: 18px; }
  .map {
    height: 180px;
    background: linear-gradient(135deg, #dfe6d6 0%, #cfdbe6 55%, #b9cde0 100%);
    border: 1px solid var(--line);
  }
  .contact-body { display: grid; grid-template-columns: 1fr 1fr 1fr; gap: 16px; margin-top: 16px; }
  .contact-details li {
    list-style: none; display: flex; gap: 7px; align-items: flex-start;
    font-size: 8.5px; color: var(--ink); line-height: 1.4; margin-bottom: 9px;
  }
  .contact-details svg { flex: 0 0 10px; margin-top: 1px; }
  .field { margin-bottom: 8px; }
  .field label { display: block; font-size: 8px; color: var(--muted); margin-bottom: 3px; }
  .field .box { height: 18px; border: 1px solid var(--line); background: #fafafa; }
  .field .box.tall { height: 70px; }
  .send {
    display: block; margin-left: auto; margin-top: 6px;
    background: var(--brand-green); color: #fff; border: 0;
    font-family: "Open Sans", Arial, sans-serif; font-size: 8.5px; font-weight: 600;
    padding: 6px 12px;
  }

  .site-footer {
    height: 64px; background: var(--footer); border-top: 1px solid var(--line);
    display: flex; align-items: center; justify-content: space-between; padding: 0 60px;
  }
  .footer-info { font-size: 8px; line-height: 1.55; color: var(--muted); }
  .footer-info strong { color: var(--ink); font-weight: 700; }
  .social { display: flex; gap: 10px; }
  .social span { width: 14px; height: 14px; border-radius: 50%; background: #555a60; display: block; }
</style>
</head>
<body>
  <header class="site-header">
    <div class="brand">
      <span class="brand-dot"></span>
      <span class="brand-name">Brindle Counseling</span>
    </div>
    <nav class="main-nav">
      <a class="current" href="#">HOME</a>
      <a href="#">ABOUT ME</a>
      <a href="#">RATES AND SERVICES</a>
      <a href="#">COMMON QUESTIONS</a>
      <a href="#">CONTACT</a>
    </nav>
  </header>

  <section class="hero">
    <div class="hero-portrait" role="img" aria-label="Portrait of therapist Martin Hale"></div>
    <h1 class="hero-title">HAPPY &amp; <b>FULFILLED</b></h1>
  </section>

  <section class="services">
    <h2 class="section-title">WHAT <span>I SERVE?</span></h2>
    <div class="service-grid">
      <article class="service">
        <div class="service-icon"><svg width="18" height="18" viewBox="0 0 18 18"><circle cx="9" cy="6" r="3.5" fill="#fff"/><path d="M2 17c0-4 3-6 7-6s7 2 7 6z" fill="#fff"/></svg></div>
        <h3>THERAPY FOR INDIVIDUALS</h3>
        <p>One-on-one sessions in a calm, private space, shaped around your goals and pace.</p>
        <a class="read-more">Read more</a>
      </article>
      <article class="service">
        <div class="service-icon"><svg width="18" height="18" viewBox="0 0 18 18"><path d="M9 16s-7-4.5-7-9a3.6 3.6 0 0 1 7-1.3A3.6 3.6 0 0 1 16 7c0 4.5-7 9-7 9z" fill="#fff"/></svg></div>
        <h3>ANXIETY, PANIC, PHOBIAS</h3>
        <p>Practical tools to ease worry, calm the body and face fear step by step.</p>
        <a class="read-more">Read more</a>
      </article>
      <article class="service">
        <div class="service-icon"><svg width="18" height="18" viewBox="0 0 18 18"><path d="M2 3h14v9H7l-4 3v-3H2z" fill="#fff"/></svg></div>
        <h3>CONSULTATIONS</h3>
        <p>A short first meeting to talk through needs and see if we are a good fit.</p>
        <a class="read-more">Read more</a>
      </article>
      <article class="service">
        <div class="service-icon"><svg width="18" height="18" viewBox="0 0 18 18"><path d="M3 9.5l4 4 8-9" stroke="#fff" stroke-width="2.4" fill="none"/></svg></div>
        <h3>SERVICES</h3>
        <p>Rates, insurance and session options explained clearly so you can plan with ease.</p>
        <a class="read-more">Read more</a>
      </article>
    </div>
  </section>

  <section class="latest">
    <h2 class="section-title">LATEST <span>WORKS</span></h2>
    <div class="post-grid">
      <article class="post">
        <div class="post-thumb" role="img" aria-label="Article image"></div>
        <div><h4>FINDING CALM DAILY</h4><p>Simple habits that help quiet a busy mind through the working week.</p></div>
      </article>
      <article class="post">
        <div class="post-thumb" role="img" aria-label="Article image"></div>
        <div><h4>REBUILDING AFTER LOSS</h4><p>Grief moves at its own pace; here are gentle ways to carry it.</p></div>
      </article>
      <article class="post">
        <div class="post-thumb" role="img" aria-label="Article image"></div>
        <div><h4>SLEEP AND THE ANXIOUS MIND</h4><p>Why worry peaks at night and what you can do to rest.</p></div>
      </article>
    </div>
  </section>

  <section class="contact">
    <h2 class="section-title">CONTACT <span>INFO</span></h2>
    <div class="map" role="img" aria-label="Map showing the office location"></div>
    <div class="contact-body">
      <ul class="contact-details">
        <li><svg width="10" height="12" viewBox="0 0 10 12"><path d="M5 0a4 4 0 0 0-4 4c0 3 4 8 4 8s4-5 4-8a4 4 0 0 0-4-4z" fill="#5b9d3c"/><circle cx="5" cy="4" r="1.5" fill="#fff"/></svg><span>Martin Hale, Licensed Counselor<br>4318 Cedarbend Ave. E, Lakewood, WA 98499</span></li>
        <li><svg width="10" height="10" viewBox="0 0 10 10"><path d="M2 0l2 2.5-1 1.2a6 6 0 0 0 3.3 3.3l1.2-1L10 8l-1.5 2C4 10 0 6 0 1.5z" fill="#5b9d3c"/></svg><span>(555) 010-0148</span></li>
        <li><svg width="10" height="8" viewBox="0 0 10 8"><rect width="10" height="8" fill="#5b9d3c"/><path d="M0 0l5 4 5-4" stroke="#fff" fill="none"/></svg><span>hello@brindlecounseling.example</span></li>
      </ul>
      <div>
        <div class="field"><label>Your Name</label><div class="box"></div></div>
        <div class="field"><label>Your Email</label><div class="box"></div></div>
        <div class="field"><label>Subject</label><div class="box"></div></div>
      </div>
      <div>
        <div class="field"><label>Message</label><div class="box tall"></div></div>
        <button class="send">Send Message</button>
      </div>
    </div>
  </section>

  <footer class="site-footer">
    <div class="footer-info">
      <strong>Brindle Counseling, PLLC</strong><br>
      Martin Hale · (555) 010-0148<br>
      © 2024 Brindle Counseling. All rights reserved.
    </div>
    <div class="social"><span></span><span></span><span></span></div>
  </footer>
</body>
</html>
```